FACIAL COSMETICS BUSINESS CARD

WE ARE A DENTAL PRACTICE BUT ARE OPENING UP A BRANCH FOR FACILA COSMETICS, LIKE BOTOX, FILLERS, PEELS, ETC. MAEVE AND ISOLDA WILL BE RUNNING THAT PART OF THE BUSINESS.
OUR CURRENT CARD IS ATTACHED AND OUR LOGO IT ATTACHED TOO. THE LOGO HAS ON IT OVEN DENTAL, I WOULD LIKE IT TO SAY OVEN COSMETICS, THE PHONE NUMBERS ON IT HAS TO BE REPLACED BY THE ONES I GAVE PREVIOUSLY AND THE WEB ADDRESS HAS TO BE DELETED, THE OTHER SIDE OF THE CARD HAS A MAP WHICH HAS TO BE DELETED, ADD TWO DATE-TIME LINES, I LIKE THE CARDS TO BE SIMPLE AND CLEAN, SIZE HAS TO BE NO LARGER THAN 5CMx8.5CM.
THE CARD HAS TO BE MATTE, I HATE GLOSSY, ABLE TO BE WRITTEN ON BOTH SIDES

Updates
I HAVE ATTACHED THE FILES, THEY CONSIST OF OUR CURRENT LOGO IN A FEW FORMS AND OUR BUSINESS CARD FOR THE DENTAL BRANCH, PLEASE COPY THE CURRENT DESIGN BUT ADDING THE REQUESTED CHANGES

Industry/Entity Type
Business
Contact Information for Business Card
OVEN COSMETICS
MAEVE : 0438 572 913
ISOLDA : 0429 638 207
SUITE 8 COLWOOD PARK ARCADE
74-86 HALBERT STREET
COLWOOD PARK NSW 2284
Logo Text
OVEN COSMETICS
Look and feel

```html
<!DOCTYPE html>
<html lang="en">
<head>
<meta charset="utf-8">
<title>Oven Cosmetics – Business Card</title>
<link rel="stylesheet" href="https://fonts.googleapis.com/css2?family=Open+Sans:wght@400;600&family=Michroma&display=swap">
<style>
  :root {
    --backdrop: #808080;
    --card-green: #3daf4a;
    --paper: #ffffff;
    --ink: #1f1f1f;
    --dot-green: #3daf4a;
  }
  * { margin: 0; padding: 0; box-sizing: border-box; }
  html, body { width: 1200px; height: 900px; overflow: hidden; }
  body { background: var(--backdrop); position: relative; font-family: "Open Sans", sans-serif; }

  .card {
    position: absolute;
    background: var(--card-green);
    overflow: hidden;
    box-shadow: 3px 4px 5px rgba(0,0,0,0.45);
  }
  .card--front { left: 178px; top: 12px; width: 710px; height: 418px; }
  .card--back  { left: 176px; top: 456px; width: 712px; height: 418px; }

  .oval { position: absolute; background: var(--paper); border-radius: 50%; }
  .card--front .oval { left: -74px; top: 80px; width: 412px; height: 268px; }
  .card--back .oval  { left: 22px; top: 28px; width: 662px; height: 358px; }

  .brand-mark {
    position: absolute; left: 10px; top: 178px; width: 270px;
    text-align: center; color: var(--ink); font-weight: 600; line-height: 1;
  }
  .brand-mark__name { display: block; font-size: 50px; letter-spacing: 3px; }
  .brand-mark__line { display: block; font-size: 22px; letter-spacing: 6px; margin-top: 6px; }

  .title {
    position: absolute; left: 380px; top: 94px; width: 246px;
    text-align: center; color: var(--paper); font-weight: 400; line-height: 1.25;
  }
  .title__top { display: block; font-size: 31px; letter-spacing: 1px; }
  .title__bottom { display: block; font-size: 35px; letter-spacing: 1px; }

  .contacts { position: absolute; left: 386px; top: 214px; color: var(--paper); font-size: 19px; letter-spacing: 0.5px; }
  .contacts li { list-style: none; height: 42px; display: flex; }
  .contacts__name { display: inline-block; width: 86px; }
  .contacts li:nth-child(2) .contacts__name { width: auto; margin-right: 4px; }

  .address {
    position: absolute; left: 290px; top: 314px; width: 406px;
    text-align: center; color: var(--paper);
    font-family: "Michroma", sans-serif; font-size: 11.5px; letter-spacing: 3px; line-height: 21px;
  }

  .appointment {
    position: absolute; left: 141px; display: flex; align-items: baseline;
    font-size: 17px; font-weight: 600; color: var(--ink);
  }
  .appointment--first { top: 138px; }
  .appointment--second { top: 274px; }
  .appointment__label { margin-right: 7px; }
  .appointment__blank {
    display: inline-block; width: 126px; height: 2px;
    border-bottom: 2px dotted var(--dot-green);
  }
  .appointment__blank--date { margin-right: 36px; }
</style>
</head>
<body>
  <section class="card card--front" aria-label="Card front">
    <div class="oval"></div>
    <div class="brand-mark">
      <span class="brand-mark__name">OVEN</span>
      <span class="brand-mark__line">COSMETICS</span>
    </div>
    <h1 class="title">
      <span class="title__top">OVEN</span>
      <span class="title__bottom">Cosmetics</span>
    </h1>
    <ul class="contacts">
      <li><span class="contacts__name">MAEVE</span><span>: 0438 572 913</span></li>
      <li><span class="contacts__name">ISOLDA</span><span>: 0429 638 207</span></li>
    </ul>
    <address class="address">
      SUITE 8 COLWOOD PARK ARCADE<br>
      74-86 HALBERT STREET,<br>
      COLWOOD PARK NSW 2284
    </address>
  </section>

  <section class="card card--back" aria-label="Card back">
    <div class="oval"></div>
    <div class="appointment appointment--first">
      <span class="appointment__label">Date :</span><span class="appointment__blank appointment__blank--date"></span>
      <span class="appointment__label">Time :</span><span class="appointment__blank"></span>
    </div>
    <div class="appointment appointment--second">
      <span class="appointment__label">Date :</span><span class="appointment__blank appointment__blank--date"></span>
      <span class="appointment__label">Time :</span><span class="appointment__blank"></span>
    </div>
  </section>
</body>
</html>
```